A modern web page for a software product

We need a web page for a software product, which is an advanced solution based on Machine Learning and Natural Language processing. We already have a logo of the product and expect the web page to be inline with the logo colors. The design should be for one page web site with scrolled sections - details of the content and guidelines in the attachments.

Target Market(s)

software company

Industry/Entity Type

It Company

Number of Pages Required

1 page

Colors

Designer to choose colors to be used in the design.

Requirements
Must have
• - modern icons and graphics
• - inline with the logo colors
• - be related to Machine Learining, AI, data processing
• - should have two language versions: english and polish both are attached.
Nice to have
• - animation/motion
Should not have
• - any photos embedded

```html
<!DOCTYPE html>
<html lang="en">
<head>
<meta charset="utf-8">
<title>DATIQ – Discovery &amp; Classification of Personal Data</title>
<link href="https://fonts.googleapis.com/css2?family=Poppins:wght@400;500;600;700&family=Open+Sans:wght@400;600&display=swap" rel="stylesheet">
<style>
:root{
  --navy:#1d3b6f;
  --navy-dark:#14284d;
  --teal:#17b3ae;
  --ink:#333a44;
  --muted:#5b6270;
  --light-bg:#f4f4f4;
  --footer:#1f2022;
  --footer-bottom:#18191b;
  --white:#ffffff;
  --partner:#9a9da3;
}
*{margin:0;padding:0;box-sizing:border-box}
html,body{width:1200px;height:2961px;overflow:hidden}
body{font-family:"Open Sans",Arial,sans-serif;color:var(--ink);background:var(--white);position:relative}
.section{position:absolute;left:0;width:1200px}
.abs{position:absolute}
.heading{font-family:"Poppins",Arial,sans-serif;font-weight:600;color:var(--ink)}

/* hero */
.hero{top:0;height:638px;overflow:hidden}
.hero-visual{position:absolute;inset:0;background:radial-gradient(ellipse at 50% 30%,#1d5a66 0%,#0f2a36 40%,#081319 75%)}
.hero-tablet{position:absolute;left:280px;top:505px;width:640px;height:30px;border-radius:6px;background:linear-gradient(180deg,#7fd2cf,#3a8e8d);opacity:.55}
.brand{font-family:"Poppins",Arial,sans-serif;font-weight:700;color:var(--white);font-size:44px;letter-spacing:1px;line-height:1}
.hero .brand{left:99px;top:32px}
.nav{left:414px;top:44px;display:flex;gap:0;align-items:center}
.nav a{font-family:"Poppins",Arial,sans-serif;font-weight:500;font-size:15px;color:var(--white);text-decoration:none;margin-right:32px}
.lang{display:flex;align-items:center;gap:6px;font-family:"Poppins",Arial,sans-serif;font-size:14px;color:var(--white)}
.hero-title{left:0;width:1200px;top:254px;text-align:center;font-family:"Poppins",Arial,sans-serif;font-weight:600;font-size:43px;line-height:52px;color:var(--white);letter-spacing:.5px}
.btn{display:inline-block;background:var(--teal);color:var(--white);font-family:"Poppins",Arial,sans-serif;font-weight:500;font-size:14px;text-align:center}
.hero .btn{left:541px;top:386px;width:118px;height:36px;line-height:36px;border-radius:2px}
.slide-arrow{width:34px;height:34px;border-radius:50%;background:rgba(0,0,0,.45);top:343px}

/* welcome */
.welcome{top:638px;height:842px}
.welcome h2{left:0;width:1200px;top:42px;text-align:center;font-size:35px}
.welcome .intro{left:140px;width:920px;top:104px;text-align:center;font-size:13px;line-height:24px;color:var(--muted)}
.features-ring{left:0;top:0}
.center-brand{left:448px;top:330px;width:300px;text-align:center}
.center-brand .brand{color:var(--navy);font-size:70px}
.center-brand .label{font-family:"Poppins",Arial,sans-serif;font-weight:600;font-size:33px;line-height:44px;color:var(--ink);margin-top:22px}
.feature-text{font-size:14px;line-height:22px;color:var(--muted);width:250px}
.feature-text.left{text-align:right}
.feature-text.center{text-align:center;width:300px}

/* use cases */
.use-cases{top:1480px;height:474px;background:var(--light-bg)}
.monitor{left:99px;top:75px;width:306px;height:311px}
.use-cases h2{left:476px;top:90px;font-size:33px}
.case{display:flex;gap:16px;align-items:flex-start;width:300px}
.case-icon{flex:none;width:42px;height:42px;border-radius:50%;border:2px solid var(--navy);display:flex;align-items:center;justify-content:center}
.case p{font-family:"Poppins",Arial,sans-serif;font-size:13px;line-height:24px;color:var(--navy);font-weight:500}

/* highlights */
.highlights{top:1954px;height:488px;background:linear-gradient(180deg,#2c4f8d 0%,#203f7a 60%,#1b3566 100%)}
.highlights h2{left:0;width:1200px;text-align:center;top:56px;font-size:33px;color:var(--white)}
.card{top:140px;width:239px;height:269px;background:var(--white)}
.card-visual{height:190px}
.card p{height:79px;display:flex;align-items:center;justify-content:center;text-align:center;padding:0 16px;font-size:14px;line-height:22px;color:var(--ink)}

/* partners */
.partners{top:2442px;height:114px;background:var(--light-bg);display:flex;justify-content:space-around;align-items:center;padding:0 100px}
.partner{font-family:"Poppins",Arial,sans-serif;font-weight:600;font-size:28px;color:var(--partner)}

/* footer */
.footer{top:2556px;height:296px;background:var(--footer);color:#d7d9dc}
.footer h3{font-family:"Poppins",Arial,sans-serif;font-weight:500;font-size:20px;color:var(--white);top:62px}
.links{left:97px;top:116px;list-style:none;font-size:13px;line-height:22.5px}
.links li::before{content:"›";margin-right:14px;color:#bbb}
.contact{left:288px;top:106px;font-size:14px;line-height:22px}
.contact-row{display:flex;gap:14px;margin-bottom:18px}
.contact-row svg{flex:none;margin-top:4px}
.quote-text{left:634px;top:100px;width:470px;font-size:12px;line-height:22px}
.field{width:227px;height:42px;border:1px solid #c9cbce;font-size:12px;line-height:40px;padding-left:14px;color:var(--white)}
.footer .btn{width:227px;height:42px;line-height:42px;font-size:13px}
.bottom-bar{top:2852px;height:109px;background:var(--footer-bottom);border-top:1px solid #2d2e31}
.copyright{left:99px;top:46px;font-size:13px;color:#d7d9dc}
.bottom-bar .brand{left:0;width:1200px;text-align:center;top:30px;font-size:44px;color:var(--navy)}
.social{left:996px;top:38px;display:flex;gap:6px}
.social span{width:24px;height:24px;border-radius:50%;border:1px solid #9ea1a6}
</style>
</head>
<body>

<!-- HERO -->
<header class="section hero">
  <div class="hero-visual" role="img" aria-label="Person in a dark suit holding a glowing tablet with a circuit-board brain hologram above it"></div>
  <div class="hero-tablet"></div>
  <div class="abs brand">DATIQ</div>
  <nav class="abs nav">
    <a>HOME</a><a>FEATURES</a><a>USE CASES</a><a>HIGHLIGHTS</a><a>ABOUT</a><a>CONTACT</a>
    <span class="lang">
      <svg width="22" height="14" viewBox="0 0 22 14"><rect width="22" height="14" fill="#2a4a9a"/><path d="M0 0L22 14M22 0L0 14" stroke="#fff" stroke-width="3"/><path d="M11 0V14M0 7H22" stroke="#fff" stroke-width="4"/><path d="M11 0V14M0 7H22" stroke="#d22" stroke-width="2"/></svg>
      English
      <svg width="8" height="5" viewBox="0 0 8 5"><path d="M0 0H8L4 5Z" fill="#fff"/></svg>
    </span>
  </nav>
  <h1 class="abs hero-title">DISCOVERY &amp; CLASSIFICATION<br>OF PERSONAL DATA</h1>
  <a class="abs btn">READ MORE</a>
  <svg class="abs slide-arrow" style="left:34px" viewBox="0 0 34 34"><path d="M19 11L13 17L19 23" stroke="#fff" stroke-width="2" fill="none"/></svg>
  <svg class="abs slide-arrow" style="left:1128px" viewBox="0 0 34 34"><path d="M15 11L21 17L15 23" stroke="#fff" stroke-width="2" fill="none"/></svg>
</header>

<!-- WELCOME / FEATURES -->
<section class="section welcome">
  <h2 class="abs heading">WELCOME TO DATIQ</h2>
  <p class="abs intro">Sed ut perspiciatis unde omnis iste natus error sit voluptatem accusantium doloremque laudantium, totam rem aperiam, eaque ipsa quae ab illo inventore veritatis et quasi architecto beatae vitae dicta sunt explicabo. Nemo enim ipsam voluptatem quia voluptas sit aspernatur aut odit aut fugit, sed quia consequuntur magni dolores eos qui ratione voluptatem sequi nesciunt. Neque porro quisquam est</p>

  <svg class="abs features-ring" width="1200" height="842" viewBox="0 0 1200 842">
    <defs>
      <linearGradient id="ringGrad" x1="0" y1="0" x2="1" y2="1">
        <stop offset="0" stop-color="#17b3ae"/><stop offset="1" stop-color="#1d3b6f"/>
      </linearGradient>
    </defs>
    <circle cx="598" cy="448" r="218" fill="none" stroke="url(#ringGrad)" stroke-width="4"/>
    <!-- teal nodes -->
    <g fill="#17b3ae">
      <circle cx="422" cy="317" r="41"/>
      <circle cx="381" cy="463" r="41"/>
      <circle cx="442" cy="607" r="41"/>
    </g>
    <!-- navy nodes -->
    <g fill="#1d3b6f">
      <circle cx="598" cy="665" r="41"/>
      <circle cx="754" cy="609" r="41"/>
      <circle cx="817" cy="462" r="41"/>
      <circle cx="772" cy="317" r="41"/>
    </g>
    <g stroke="#fff" stroke-width="3" fill="none" stroke-linecap="round" stroke-linejoin="round">
      <!-- unlock -->
      <rect x="409" y="316" width="26" height="20" rx="2"/><path d="M415 316v-8a9 9 0 0 1 17-3"/>
      <!-- database -->
      <ellipse cx="381" cy="449" rx="13" ry="5"/><path d="M368 449v28c0 3 6 5 13 5s13-2 13-5v-28M368 458c0 3 6 5 13 5s13-2 13-5M368 467c0 3 6 5 13 5s13-2 13-5"/>
      <!-- edit -->
      <rect x="428" y="596" width="22" height="22" rx="2"/><path d="M440 606l14-14 4 4-14 14h-4z"/>
      <!-- laptop -->
      <rect x="584" y="653" width="28" height="18" rx="1"/><path d="M578 676h40"/>
      <!-- sitemap -->
      <rect x="748" y="594" width="12" height="9"/><rect x="738" y="617" width="10" height="8"/><rect x="750" y="617" width="10" height="8"/><rect x="762" y="617" width="10" height="8"/><path d="M754 603v7M743 617v-7h24v7M755 610v7"/>
      <!-- chart -->
      <rect x="802" y="448" width="30" height="28"/><path d="M807 470l7-8 6 4 8-10"/>
    </g>
    <!-- users -->
    <g fill="#fff">
      <circle cx="772" cy="306" r="7"/><path d="M760 330c0-9 5-14 12-14s12 5 12 14z"/>
      <circle cx="759" cy="310" r="5"/><path d="M750 328c0-7 3-10 9-10l2 1c-2 2-3 5-3 9z"/>
      <circle cx="785" cy="310" r="5"/><path d="M794 328c0-7-3-10-9-10l-2 1c2 2 3 5 3 9z"/>
    </g>
  </svg>

  <div class="abs center-brand">
    <div class="brand">DATIQ</div>
    <div class="label">MAIN<br>FEATURES</div>
  </div>

  <p class="abs feature-text left" style="left:111px;top:286px">Detection of personal and sensitive data for GDPR compliance</p>
  <p class="abs feature-text left" style="left:68px;top:418px">Fast cataloging and classification of data and sources</p>
  <p class="abs feature-text left" style="left:126px;top:588px">Unified data registry for RODO compliance fulfilment</p>
  <p class="abs feature-text center" style="left:448px;top:726px">RESTful API for system management and integration</p>
  <p class="abs feature-text" style="left:823px;top:588px">Ability to integrates with tools for data anonymization or depersonalization</p>
  <p class="abs feature-text" style="left:883px;top:432px">Customizable analytics and reporting</p>
  <p class="abs feature-text" style="left:839px;top:278px">Management of consents and data access policies</p>
</section>

<!-- USE CASES -->
<section class="section use-cases">
  <div class="abs monitor" role="img" aria-label="Desktop computer monitor displaying a machine learning interface with keyboard and mouse" style="background:linear-gradient(180deg,#2a4f8f 0%,#4f79b8 55%,#d9dde2 76%,#eceef0 100%);border-radius:6px"></div>
  <h2 class="abs heading">USE CASES</h2>

  <div class="abs case" style="left:476px;top:172px">
    <span class="case-icon"><svg width="20" height="18" viewBox="0 0 20 18"><path d="M10 2c5 0 8 3 8 6s-3 6-8 6l-5 3 1-4c-3-1-4-3-4-5 0-3 3-6 8-6z" fill="none" stroke="#1d3b6f" stroke-width="2"/></svg></span>
    <p>Internal audits and verification of the current status - in preparation for ensuring RODO compliance RODO</p>
  </div>
  <div class="abs case" style="left:476px;top:292px">
    <span class="case-icon"><svg width="18" height="18" viewBox="0 0 18 18"><circle cx="9" cy="5" r="4" fill="#1d3b6f"/><path d="M1 18c0-5 4-8 8-8s8 3 8 8z" fill="#1d3b6f"/></svg></span>
    <p>Keeping the registry of personal data in order to implement rights to information,forgetfulness, data transfer</p>
  </div>
  <div class="abs case" style="left:827px;top:178px">
    <span class="case-icon"><svg width="16" height="18" viewBox="0 0 16 18"><ellipse cx="8" cy="3" rx="7" ry="2.5" fill="#1d3b6f"/><path d="M1 5c0 2 14 2 14 0v3c0 2-14 2-14 0zM1 10c0 2 14 2 14 0v3c0 3-14 3-14 0z" fill="#1d3b6f"/></svg></span>
    <p>Cataloging sources that store sensitive data</p>
  </div>
  <div class="abs case" style="left:827px;top:255px">
    <span class="case-icon"><svg width="20" height="18" viewBox="0 0 20 18"><rect x="2" y="2" width="16" height="11" fill="none" stroke="#1d3b6f" stroke-width="2"/><path d="M6 16h8" stroke="#1d3b6f" stroke-width="2"/></svg></span>
    <p>Continuous monitoring and classification of data</p>
  </div>
  <div class="abs case" style="left:827px;top:332px">
    <span class="case-icon"><svg width="20" height="18" viewBox="0 0 20 18"><path d="M2 2v14h16" fill="none" stroke="#1d3b6f" stroke-width="2"/><path d="M5 12l4-5 3 3 5-6" fill="none" stroke="#1d3b6f" stroke-width="2"/></svg></span>
    <p>Use collected the data to create additional business value,</p>
  </div>
</section>

<!-- HIGHLIGHTS -->
<section class="section highlights" role="img" aria-label="Dark blue background with a blurred office scene" >
  <h2 class="abs heading">HIGHLIGHTS</h2>
  <div class="abs card" style="left:99px">
    <div class="card-visual" role="img" aria-label="Hand holding a tablet showing a data management dashboard" style="background:linear-gradient(160deg,#c9d3dc,#5b7ea6 55%,#2f4a6d)"></div>
    <p>Built in support for detection of Polish personal data</p>
  </div>
  <div class="abs card" style="left:351px">
    <div class="card-visual" role="img" aria-label="Businesswoman touching a digital process diagram" style="background:linear-gradient(160deg,#0f3e4e,#1d6f80 50%,#0c2d3a)"></div>
    <p>High effectiveness of personal data detection by combining</p>
  </div>
  <div class="abs card" style="left:606px">
    <div class="card-visual" role="img" aria-label="Businessman holding a laptop with sketched network lines around it" style="background:linear-gradient(160deg,#5a5f66,#2a2d31 60%,#4b4f55)"></div>
    <p>Supports structured and unstructured data source</p>
  </div>
  <div class="abs card" style="left:861px">
    <div class="card-visual" role="img" aria-label="Thoughtful woman beside a hand-drawn business diagram on a white wall" style="background:linear-gradient(160deg,#f1f1f1,#d9d9d9 60%,#c4c4c4)"></div>
    <p>Ready for high performance processing</p>
  </div>
</section>

<!-- PARTNERS -->
<section class="section partners">
  <span class="partner">VERTEX</span>
  <span class="partner">Lumora</span>
  <span class="partner">ARCHON</span>
  <span class="partner">Kelvo</span>
  <span class="partner">brightly</span>
  <span class="partner">NORDA</span>
</section>

<!-- FOOTER -->
<footer class="section footer">
  <h3 class="abs" style="left:97px">QUICK LINK</h3>
  <ul class="abs links">
    <li>Home</li><li>Features</li><li>Use Cases</li><li>Highlights</li><li>About</li><li>Contact</li>
  </ul>

  <h3 class="abs" style="left:288px">CONTACT US</h3>
  <div class="abs contact">
    <div class="contact-row"><svg width="12" height="16" viewBox="0 0 12 16"><path d="M6 0a6 6 0 0 1 6 6c0 4-6 10-6 10S0 10 0 6a6 6 0 0 1 6-6z" fill="#fff"/><circle cx="6" cy="6" r="2.2" fill="#1f2022"/></svg><span>420 Harbor Lane, Suite 12 Austin,<br>Texas 78701, United States</span></div>
    <div class="contact-row"><svg width="14" height="14" viewBox="0 0 14 14"><path d="M3 0l3 3-2 2c1 2 3 4 5 5l2-2 3 3-2 3C6 14 0 8 0 3z" fill="#fff"/></svg><span>Phone : 555-014-2290</span></div>
    <div class="contact-row"><svg width="14" height="11" viewBox="0 0 14 11"><rect width="14" height="11" fill="#fff"/><path d="M0 0l7 6 7-6" stroke="#1f2022" stroke-width="1.5" fill="none"/></svg><span>Email : info@datiq.example</span></div>
  </div>

  <h3 class="abs" style="left:634px">GET A QUOTE</h3>
  <p class="abs quote-text">Lorem ipsum dolor sit amet, consectetur adipiscing elit, sed do eiusmod tempor incididunt ut labore et dolore magna aliqua. Ut enim ad minim veniam,</p>
  <div class="abs field" style="left:634px;top:146px">Name</div>
  <div class="abs field" style="left:874px;top:146px">E - Mail</div>
  <div class="abs field" style="left:634px;top:198px">Phone No</div>
  <a class="abs btn" style="left:874px;top:198px">SUBMIT NOW!</a>
</footer>

<div class="section bottom-bar">
  <p class="abs copyright">© 2018 datiq. All Rights Reserved.</p>
  <div class="abs brand">DATIQ</div>
  <div class="abs social"><span></span><span></span><span></span><span></span></div>
</div>

</body>
</html>
```